Business Card Design Project - KLB

I am looking for a more sophisticated card design for my company,
"The Kestrel Bureau"

We are a consultancy focused on strategy and change in Associations and professional organisations.

I am a lawyer and psychologist with a PhD and so am looking for something that communicates seriousness and credibility but also quirky creative solutions for strategic problems, which is my field of speciality.

I am looking for something that is quietly spoken, rather than loud colours ('credible' and 'creative' are the two adjectives that I think of as competing here).

I particularly like an embossed card style - heavy white card with plain white or white and black or white and grey text.

The key logo image for the company is a question mark and I am open to suggestions and ideas on design.

I have attached a file that includes a couple of styles that have caught my eye and my thoughts on them. Hopefully they communicate what I'm looking for.
Updates

Thank you for all the great suggestions and designs.

I really appreciated the effort and creative energy you put into your designs. I have now closed the project after selecting a design and advising the successful designer of the card that I am happy with.

Regards

Target Market(s)

Organisations (CEO's and Boards), Governments, Legal professionals, Membership Associations and aspiring professionals.

Industry/Entity Type

Lawyer

Requirements
Must have
• The key logo element is a question mark (?) and this needs to be incorporated.

Embossed style - cut outs or other design ideas interest me too.

The attached file has a number of sample ideas and comments on each one that I like.
Should not have
• I like crisp, modern fonts (Myriads etc...) and do not like embellished fonts or Times etc...

```html
<!DOCTYPE html>
<html lang="en">
<head>
<meta charset="utf-8">
<title>The Kestrel Bureau — Business Card</title>
<link rel="stylesheet" href="https://fonts.googleapis.com/css2?family=Arimo:wght@400;700&display=swap">
<style>
  :root {
    --backdrop: #1c1c1c;
    --card-white: #f3f3f1;
    --card-edge: #dcdcd8;
    --ink-dark: #3a3a3a;
    --ink-mid: #6b6b6b;
    --ink-soft: #8d8d8d;
    --mark-grey: #bdbdbb;
  }
  * { margin: 0; padding: 0; box-sizing: border-box; }
  html, body {
    width: 1200px;
    height: 1052px;
    overflow: hidden;
    background: var(--backdrop);
    font-family: "Arimo", Arial, sans-serif;
  }
  .stage {
    width: 1200px;
    height: 1052px;
    display: flex;
    align-items: center;
    justify-content: center;
  }
  .card {
    position: relative;
    width: 900px;
    height: 520px;
    background: var(--card-white);
    border-top-left-radius: 110px;
    border: 1px solid var(--card-edge);
  }
  .brand {
    position: absolute;
    top: 78px;
    left: 78px;
    display: flex;
    align-items: center;
    gap: 22px;
  }
  .brand-square {
    width: 64px;
    height: 64px;
    background: var(--mark-grey);
  }
  .brand-name {
    font-weight: 700;
    font-size: 44px;
    letter-spacing: 2px;
    color: var(--ink-mid);
  }
  .contact {
    position: absolute;
    right: 70px;
    top: 280px;
    text-align: right;
    color: var(--ink-dark);
  }
  .contact-name {
    font-weight: 700;
    font-size: 34px;
    letter-spacing: 4px;
    text-shadow: 0 1px 0 #ffffff, 0 -1px 0 rgba(0,0,0,0.15);
    margin-bottom: 22px;
  }
  .contact-line {
    font-size: 15px;
    letter-spacing: 2.5px;
    color: var(--ink-soft);
    margin-bottom: 16px;
  }
  .contact-line .divider { margin: 0 14px; }
</style>
</head>
<body>
  <main class="stage">
    <article class="card">
      <header class="brand">
        <span class="brand-square" aria-hidden="true"></span>
        <span class="brand-name">The Kestrel Bureau</span>
      </header>
      <section class="contact">
        <h1 class="contact-name">Dr. Mara Ellison</h1>
        <p class="contact-line">M::: +61400 000 111<span class="divider">|</span>P::: +612 9000 2233</p>
        <p class="contact-line">P.O. Box 4410, Lane Cove, Sydney, Australia</p>
        <p class="contact-line">mara@kestrelbureau.com.au</p>
      </section>
    </article>
  </main>
</body>
</html>
```